Business Card Design

We need a business card designed to the point of print ready to take to our printers. the design should be professional, easy to read and simple. The cards should represent our business as professional and trust worthy.

Attached are several versions o the logo, and also the details for the card to be printed. please do communicate if different versions of the logo is required.

Business

```html
<!DOCTYPE html>
<html lang="en">
<head>
<meta charset="utf-8">
<title>Tallyway Pty Ltd – Business Cards</title>
<link href="https://fonts.googleapis.com/css2?family=Noto+Sans:wght@400;700&display=swap" rel="stylesheet">
<style>
  :root {
    --backdrop: #3d3d3d;
    --card-white: #ffffff;
    --card-grey: #d6d6d6;
    --swoosh: #e0b062;
    --accent: #f7941d;
    --ink: #3a3a3a;
    --mark-grey: #6b6b6b;
  }
  html, body {
    margin: 0;
    padding: 0;
    width: 1200px;
    height: 900px;
    overflow: hidden;
    background: var(--backdrop);
    font-family: "Noto Sans", Arial, sans-serif;
  }
  .canvas { position: relative; width: 1200px; height: 900px; }
  .card {
    position: absolute;
    background: var(--card-white);
    overflow: hidden;
  }
  .card-front { left: 0; top: 0; width: 858px; height: 492px; }
  .card-back { left: 506px; top: 494px; width: 694px; height: 399px; }
  .card-bg { position: absolute; inset: 0; }
  .company-name {
    position: absolute;
    margin: 0;
    color: var(--mark-grey);
    font-weight: 700;
    white-space: nowrap;
    letter-spacing: -0.5px;
  }
  .card-front .company-name { left: 18px; top: 18px; font-size: 46px; }
  .card-back .company-name {
    left: 0; right: 0; top: 104px; text-align: center;
    font-size: 58px; padding-left: 30px;
  }
  .website {
    position: absolute;
    margin: 0;
    color: var(--accent);
    white-space: nowrap;
  }
  .card-front .website { left: 500px; top: 24px; font-size: 22px; }
  .card-back .website {
    left: 0; right: 0; top: 240px; text-align: center;
    font-size: 25px; padding-left: 30px;
  }
  .holder {
    position: absolute;
    left: 250px; width: 410px; top: 184px;
    text-align: center;
  }
  .holder-name { margin: 0; font-size: 36px; color: var(--ink); font-weight: 400; letter-spacing: 0.5px; line-height: 1.1; }
  .holder-role { margin: 0; font-size: 26px; color: var(--accent); letter-spacing: 0.5px; line-height: 1.3; }
  .contact {
    position: absolute;
    right: 12px; top: 378px;
    margin: 0;
    text-align: right;
    font-size: 21px;
    color: var(--ink);
    line-height: 34px;
    font-style: normal;
    letter-spacing: 0.3px;
  }
</style>
</head>
<body>
<main class="canvas">

  <section class="card card-front" aria-label="Business card front">
    <svg class="card-bg" width="858" height="492" viewBox="0 0 858 492" aria-hidden="true">
      <ellipse cx="545" cy="205" rx="560" ry="300" transform="rotate(-12 545 205)" fill="var(--swoosh)"/>
      <ellipse cx="585" cy="185" rx="555" ry="285" transform="rotate(-12 585 185)" fill="var(--card-grey)"/>
    </svg>
    <p class="company-name">Tallyway Pty Ltd</p>
    <p class="website">www.tallyway.com.au</p>
    <div class="holder">
      <h1 class="holder-name">Joanna Perrin</h1>
      <p class="holder-role">Managing Director</p>
    </div>
    <address class="contact">
      Telephone: +61 400 555 019<br>
      Email: jperrin@tallyway.com.au<br>
      Postal: PO Box 1234 Harbour Centre Qld 4000
    </address>
  </section>

  <section class="card card-back" aria-label="Business card back">
    <svg class="card-bg" width="694" height="399" viewBox="0 0 694 399" aria-hidden="true">
      <ellipse cx="470" cy="210" rx="470" ry="290" transform="rotate(-25 470 210)" fill="var(--swoosh)"/>
      <ellipse cx="505" cy="200" rx="465" ry="280" transform="rotate(-25 505 200)" fill="var(--card-grey)"/>
    </svg>
    <p class="company-name">Tallyway Pty Ltd</p>
    <p class="website">www.tallyway.com.au</p>
  </section>

</main>
</body>
</html>
```